Flyer für dynamisches Maklerteam
The design process with Brightwing went very well. He responded precisely to our requirements and to our target group and developed designs that reflect our logo and our corporate identity in many small details. Communication with Brightwing went great. He quickly translated our requests into wonderful designs and created flyers that we are very happy with. Brightwing is a good designer and I can highly recommend working with him. Dr. Ilse Brandvoort KORVEN Real Estate
Zielgruppe
KORVEN Immobilien ist ein dynamisches Maklerteam, dass sich auf den Verkauf von Wohnimmobilien des gehobenen Preissegmentes spezialisiert hat. Unser Schwerpunkt liegt auf Luxusobjekten.
Hallo,
schön, dass ihr an unserem Design-Wettbewerb teilnehmt.
Unser Zielgruppe sind verkaufswillige Eigentümer hochpreisiger Immobilien.
--> eine ganz wichtige Kundengruppe sind Erben, die ihre geerbte Immobilie verkaufen wollen.
Wir wünschen uns beidseitig bedruckte Flyer auf hochwertigem Material (Chromosulfatpapier, 450 g/m²). Bei der Auswahl des Formates wollen wir euch freie Hand lassen.
Vorderseite:
- Logo von KORVEN Immobilien.
- Ein Foto als Eye-Catcher, das Interesse weckt, zum Schmunzeln bringt und in Erinnerung bleibt. Wichtig: Auf dem Foto sollte man Freude sehen (gerne lächelnde Gesichter, die Personen müssen nicht zwangsläufig in die Kamera blicken. Eine positive und glückliche Grundstimmung auf dem Bild ist wichtig). -> an dieser Stelle bitte geeignete Stock-Bilder recherchieren und diese vorschlagen.
- Claim: Genießen Sie Ihre Freiheit. Wir verkaufen Ihre Immobilie.
Rückseite:
folgenden Text bitte verwenden:
Das Besondere bei KORVEN Immobilien:
- langjährige Erfahrung mit Immobilien des gehobenen Segments
- hochprofessionelle Komplettabwicklung in kürzester Zeit
- ausgezeichnete Referenzen
- auf Wunsch sehr diskrete Abwicklung
Anschließend bitte einen Satz, der eine Abschlussfrage formuliert, die etwa folgenden Inhalt wiedergibt:
'Wenn Sie direkt mit uns sprechen möchten, erreichen Sie uns jederzeit unter 0157 - 3948 2036.'
(Diesen Satz könnt ihr gerne umformulieren.)
Website und Emailadresse [ www.korven-immobilien.example - ib@korven-immobilien.example ]
Bilder des gesamten KORVEN Verkaufsteam als Einzelportraits vor dunklem Hintergrund.
Dabei wichtig: Lorenz Korven als Chef bitte an die erste Stelle setzen. Henrike und Jonas Weidlich sind ein Ehepaar, die Immobilien meist gemeinsam verkaufen, daher bitte auch ihre beiden Portraits nebeneinander platzieren.
Bei der Gestaltung des Flyers i..

```html
<!DOCTYPE html>
<html lang="de">
<head>
<meta charset="utf-8">
<title>KORVEN Immobilien – Flyer</title>
<link href="https://fonts.googleapis.com/css2?family=Cinzel:wght@400;500&family=Jost:wght@400;500;600;700&display=swap" rel="stylesheet">
<style>
:root{
  --bg:#efefef;
  --navy:#1f2a6b;
  --gold:#b48a5a;
  --grey:#dcdcde;
  --dark:#16161a;
  --white:#ffffff;
  --ink:#1f2a6b;
  --tick:#2a9a3a;
}
*{box-sizing:border-box;margin:0;padding:0}
html,body{width:1200px;height:2352px;overflow:hidden;background:var(--bg)}
body{position:relative;font-family:"Jost",sans-serif}
.set{position:absolute;left:0;width:1200px;height:430px}
.front{position:absolute;left:274px;top:15px;width:297px;height:418px;background:var(--white);overflow:hidden;box-shadow:0 6px 14px rgba(0,0,0,.18)}
.back{position:absolute;left:605px;top:0;width:308px;height:430px;background:var(--white);overflow:hidden;box-shadow:0 6px 14px rgba(0,0,0,.22)}
.photo{position:absolute;left:0;top:0}
.front .photo{
  width:297px;height:345px;
  background:
    radial-gradient(ellipse 55% 40% at 95% 30%, rgba(240,140,60,.95) 0%, rgba(220,120,50,.55) 45%, rgba(220,120,50,0) 75%),
    radial-gradient(ellipse 35% 45% at 78% 72%, rgba(196,110,60,.95) 0%, rgba(170,90,50,.6) 50%, rgba(170,90,50,0) 85%),
    radial-gradient(ellipse 40% 35% at 35% 42%, rgba(110,60,38,.95) 0%, rgba(110,60,38,0) 80%),
    radial-gradient(ellipse 60% 45% at 35% 85%, rgba(135,140,148,1) 0%, rgba(120,124,132,.8) 45%, rgba(120,124,132,0) 85%),
    linear-gradient(180deg,#e6e8ea 0%,#c9cbcd 18%,#8a8580 38%,#5b5a5c 60%,#3f4145 100%);
}
.back .photo{
  width:308px;height:100px;
  background:
    radial-gradient(ellipse 35% 70% at 50% 60%, rgba(248,248,246,1) 0%, rgba(235,235,232,.9) 45%, rgba(235,235,232,0) 80%),
    radial-gradient(ellipse 30% 90% at 95% 50%, rgba(60,110,45,1) 0%, rgba(60,110,45,0) 85%),
    radial-gradient(ellipse 25% 60% at 75% 10%, rgba(70,120,55,.9) 0%, rgba(70,120,55,0) 80%),
    linear-gradient(100deg,#5c5a55 0%,#8e8a82 30%,#d9d9d6 50%,#b9b7b0 70%,#4f7a3c 100%);
}
.logo-panel{position:absolute;left:0;width:144px;height:56px}
.front .logo-panel{top:17px}
.back .logo-panel{top:0;width:110px;height:48px}
.logo-name{position:absolute;font-family:"Cinzel",serif;font-weight:500;color:var(--navy);letter-spacing:2px}
.front .logo-name{left:28px;top:32px;font-size:21px}
.back .logo-name{left:20px;top:12px;font-size:16px}
.band{position:absolute;left:0}
.claim{position:absolute;left:26px;top:364px;font-family:"Cinzel",serif;font-weight:400;font-size:14.5px;line-height:21px;color:var(--white);letter-spacing:.3px}
.claim .accent{color:var(--gold);font-size:12.5px}
.badge{position:absolute;left:207px;top:73px;width:74px;height:74px;border-radius:50%;background:var(--navy);border:3px solid var(--white);box-shadow:0 2px 6px rgba(0,0,0,.35);text-align:center;padding-top:19px;font-weight:700;font-size:8px;line-height:9.5px;transform:rotate(8deg)}
.badge .w{color:var(--white)}
.badge .g{color:var(--gold)}
.title{position:absolute;left:26px;top:117px;font-family:"Cinzel",serif;font-weight:400;font-size:11.5px;line-height:17px;color:var(--white)}
.title .accent{color:var(--gold)}
.usp{position:absolute;left:28px;top:158px;list-style:none}
.usp li{height:20px;font-size:7.5px;color:var(--white);display:flex;align-items:center;gap:8px}
.usp svg{width:11px;height:12px}
.info{position:absolute;left:0;top:250px;width:308px;height:90px;color:var(--ink)}
.info .lead{font-weight:600;font-size:5.6px;line-height:9px}
.info .item{font-size:5px;line-height:10px;display:flex;gap:5px;align-items:flex-start}
.info .contact{font-size:6.2px;font-weight:600;display:flex;align-items:center;gap:3px;line-height:11px}
.info .contact svg{width:7px;height:7px}
.col-left{position:absolute;left:22px;top:12px;width:150px}
.col-right{position:absolute;left:186px;top:20px;width:110px}
.divider{position:absolute;left:176px;top:18px;width:1px;height:56px;background:#9aa0b8}
.centered{position:absolute;left:0;top:10px;width:308px;text-align:center}
.centered .item{display:block;line-height:10px}
.centered .row{display:flex;justify-content:center;gap:10px}
.big-phone{font-size:13px;font-weight:600;display:flex;justify-content:center;align-items:center;gap:5px;margin:6px 0 4px}
.big-phone svg{width:12px;height:12px}
.team-title{position:absolute;right:34px;top:352px;font-family:"Cinzel",serif;font-weight:400;font-size:10px;color:var(--white)}
.team-title .accent{color:var(--gold)}
.team{position:absolute;left:14px;top:370px;width:280px;display:flex;justify-content:space-between}
.member{width:42px;text-align:center}
.portrait{width:42px;height:40px;border-bottom:2px solid var(--navy);
  background:
    radial-gradient(ellipse 30% 35% at 50% 38%, rgba(200,160,135,.85) 0%, rgba(200,160,135,0) 90%),
    radial-gradient(ellipse 55% 35% at 50% 100%, rgba(40,44,70,1) 0%, rgba(40,44,70,0) 95%),
    linear-gradient(180deg,#2e2e34 0%,#25252b 100%);}
.member p{font-size:4.2px;font-weight:600;color:var(--white);margin-top:4px;white-space:nowrap}
</style>
</head>
<body>

<section class="set" style="top:155px">
  <article class="front">
    <div class="photo" role="img" aria-label="Glückliches Paar von hinten vor einer modernen Villa im warmen Abendlicht"></div>
    <svg class="band" width="297" height="418" viewBox="0 0 297 418" style="top:0">
      <polygon points="0,337 297,305 297,418 0,418" fill="#1f2a6b"/>
      <polygon points="0,331 297,299 297,305 0,337" fill="#b48a5a"/>
    </svg>
    <svg class="logo-panel" viewBox="0 0 144 56"><polygon points="0,0 144,0 128,56 0,56" fill="#fff" fill-opacity=".95"/></svg>
    <div class="logo-name">KORVEN</div>
    <p class="claim"><span class="accent">GENIEẞEN</span> SIE IHRE FREIHEIT.<br>WIR VERKAUFEN <span class="accent">IHRE IMMOBILIE.</span></p>
  </article>

  <article class="back">
    <div class="photo" role="img" aria-label="Moderner weißer Bungalow mit Terrasse im Grünen"></div>
    <svg class="band" width="308" height="430" viewBox="0 0 308 430" style="top:0">
      <polygon points="0,90 308,72 308,256 0,251" fill="#1f2a6b"/>
      <polygon points="0,84 308,66 308,72 0,90" fill="#b48a5a"/>
      <polygon points="0,251 308,256 308,342 0,340" fill="#dcdcde"/>
      <polygon points="0,340 308,334 308,430 0,430" fill="#16161a"/>
    </svg>
    <svg class="logo-panel" viewBox="0 0 110 48"><polygon points="0,0 110,0 98,48 0,48" fill="#fff"/></svg>
    <div class="logo-name">KORVEN</div>
    <div class="badge"><span class="w">KOSTENLOSE</span><br><span class="g">IMMOBILIEN<br>BEWERTUNG</span></div>
    <h2 class="title">Das Besondere bei<br><span class="accent">KORVEN Immobilien</span></h2>
    <ul class="usp">
      <li><svg viewBox="0 0 11 12"><path d="M1 5 L4 10 L10 1" fill="none" stroke="#fff" stroke-width="1.6"/></svg>langjährige Erfahrung mit Immobilien des gehobenen Segments</li>
      <li><svg viewBox="0 0 11 12"><path d="M1 5 L4 10 L10 1" fill="none" stroke="#fff" stroke-width="1.6"/></svg>hochprofessionelle Komplettabwicklung in kürzester Zeit</li>
      <li><svg viewBox="0 0 11 12"><path d="M1 5 L4 10 L10 1" fill="none" stroke="#fff" stroke-width="1.6"/></svg>ausgezeichnete Referenzen</li>
      <li><svg viewBox="0 0 11 12"><path d="M1 5 L4 10 L10 1" fill="none" stroke="#fff" stroke-width="1.6"/></svg>auf Wunsch sehr diskrete Abwicklung</li>
    </ul>
    <div class="info">
      <div class="col-left">
        <p class="lead">In jeder Situation stehen wir mit unserem<br>Fachwissen an Ihrer Seite:</p>
        <p class="item"><svg width="7" height="7" viewBox="0 0 7 7"><path d="M0.5 3.5 L2.5 6 L6.5 0.5" fill="none" stroke="#2a9a3a" stroke-width="1.2"/></svg>Wenn Sie Eigentümer einer Immobilie sind oder es werden wollen</p>
        <p class="item"><svg width="7" height="7" viewBox="0 0 7 7"><path d="M0.5 3.5 L2.5 6 L6.5 0.5" fill="none" stroke="#2a9a3a" stroke-width="1.2"/></svg>Wenn Sie allein oder in Gemeinschaft eine Immobilie geerbt haben</p>
        <p class="item"><svg width="7" height="7" viewBox="0 0 7 7"><path d="M0.5 3.5 L2.5 6 L6.5 0.5" fill="none" stroke="#2a9a3a" stroke-width="1.2"/></svg>Wenn Sie eine Firma vertreten oder Investor sind</p>
      </div>
      <div class="divider"></div>
      <div class="col-right">
        <p class="lead">Sie erreichen uns<br>jederzeit unter</p>
        <p class="contact"><svg viewBox="0 0 8 8"><path d="M1.5 0.8 L3 2.6 L2.2 3.6 Q3.3 5.2 4.4 5.8 L5.4 5 L7.2 6.5 L6.2 7.5 Q2.5 6.8 0.5 1.8 Z" fill="#1f2a6b"/></svg>0157 - 3948 2036</p>
        <p class="contact"><svg viewBox="0 0 8 8"><rect x="0.5" y="1.5" width="7" height="5" fill="none" stroke="#1f2a6b" stroke-width=".8"/><path d="M0.5 1.5 L4 4.5 L7.5 1.5" fill="none" stroke="#1f2a6b" stroke-width=".8"/></svg>ib@korven-immobilien.example</p>
        <p class="contact"><svg viewBox="0 0 8 8"><circle cx="4" cy="4" r="3.4" fill="none" stroke="#1f2a6b" stroke-width=".8"/><path d="M0.6 4 H7.4 M4 0.6 V7.4" stroke="#1f2a6b" stroke-width=".6"/></svg>www.korven-immobilien.example</p>
      </div>
    </div>
    <h3 class="team-title">Unser <span class="accent">Team</span></h3>
    <div class="team">
      <div class="member"><div class="portrait" role="img" aria-label="Portrait Lorenz A. Korven vor dunklem Hintergrund"></div><p>Lorenz A. Korven</p></div>
      <div class="member"><div class="portrait" role="img" aria-label="Portrait Henrike Weidlich vor dunklem Hintergrund"></div><p>Henrike Weidlich</p></div>
      <div class="member"><div class="portrait" role="img" aria-label="Portrait Jonas Weidlich vor dunklem Hintergrund"></div><p>Jonas Weidlich</p></div>
      <div class="member"><div class="portrait" role="img" aria-label="Portrait Greta Haldenmeier vor dunklem Hintergrund"></div><p>Greta Haldenmeier</p></div>
      <div class="member"><div class="portrait" role="img" aria-label="Portrait Dr. Ilse Brandvoort vor dunklem Hintergrund"></div><p>Dr. Ilse Brandvoort</p></div>
      <div class="member"><div class="portrait" role="img" aria-label="Portrait Mira Sonntag vor dunklem Hintergrund"></div><p>Mira Sonntag</p></div>
    </div>
  </article>
</section>

<section class="set" style="top:955px">
  <article class="front">
    <div class="photo" role="img" aria-label="Glückliches Paar von hinten vor einer modernen Villa im warmen Abendlicht"></div>
    <svg class="band" width="297" height="418" viewBox="0 0 297 418" style="top:0">
      <polygon points="0,337 297,305 297,418 0,418" fill="#1f2a6b"/>
      <polygon points="0,331 297,299 297,305 0,337" fill="#b48a5a"/>
    </svg>
    <svg class="logo-panel" viewBox="0 0 144 56"><polygon points="0,0 144,0 128,56 0,56" fill="#fff" fill-opacity=".95"/></svg>
    <div class="logo-name">KORVEN</div>
    <p class="claim"><span class="accent">GENIEẞEN</span> SIE IHRE FREIHEIT.<br>WIR VERKAUFEN <span class="accent">IHRE IMMOBILIE.</span></p>
  </article>

  <article class="back">
    <div class="photo" role="img" aria-label="Moderner weißer Bungalow mit Terrasse im Grünen"></div>
    <svg class="band" width="308" height="430" viewBox="0 0 308 430" style="top:0">
      <polygon points="0,90 308,72 308,256 0,251" fill="#1f2a6b"/>
      <polygon points="0,84 308,66 308,72 0,90" fill="#b48a5a"/>
      <polygon points="0,251 308,256 308,342 0,340" fill="#dcdcde"/>
      <polygon points="0,340 308,334 308,430 0,430" fill="#16161a"/>
    </svg>
    <svg class="logo-panel" viewBox="0 0 110 48"><polygon points="0,0 110,0 98,48 0,48" fill="#fff"/></svg>
    <div class="logo-name">KORVEN</div>
    <div class="badge"><span class="w">KOSTENLOSE</span><br><span class="g">IMMOBILIEN<br>BEWERTUNG</span></div>
    <h2 class="title">Das Besondere bei<br><span class="accent">KORVEN Immobilien</span></h2>
    <ul class="usp">
      <li><svg viewBox="0 0 11 12"><path d="M1 5 L4 10 L10 1" fill="none" stroke="#fff" stroke-width="1.6"/></svg>langjährige Erfahrung mit Immobilien des gehobenen Segments</li>
      <li><svg viewBox="0 0 11 12"><path d="M1 5 L4 10 L10 1" fill="none" stroke="#fff" stroke-width="1.6"/></svg>hochprofessionelle Komplettabwicklung in kürzester Zeit</li>
      <li><svg viewBox="0 0 11 12"><path d="M1 5 L4 10 L10 1" fill="none" stroke="#fff" stroke-width="1.6"/></svg>ausgezeichnete Referenzen</li>
      <li><svg viewBox="0 0 11 12"><path d="M1 5 L4 10 L10 1" fill="none" stroke="#fff" stroke-width="1.6"/></svg>auf Wunsch sehr diskrete Abwicklung</li>
    </ul>
    <div class="info">
      <div class="centered">
        <p class="lead">In jeder Situation stehen wir mit unserem Fachwissen an Ihrer Seite:</p>
        <p class="item">- Wenn Sie Eigentümer einer Immobilie sind oder es werden wollen</p>
        <p class="item">- Wenn Sie allein oder in Gemeinschaft eine Immobilie geerbt haben</p>
        <p class="item">- Wenn Sie eine Firma vertreten oder Investor sind</p>
        <p class="lead" style="margin-top:4px">Sie erreichen uns jederzeit unter</p>
        <div class="row">
          <p class="contact"><svg viewBox="0 0 8 8"><path d="M1.5 0.8 L3 2.6 L2.2 3.6 Q3.3 5.2 4.4 5.8 L5.4 5 L7.2 6.5 L6.2 7.5 Q2.5 6.8 0.5 1.8 Z" fill="#1f2a6b"/></svg>0157 - 3948 2036</p>
          <p class="contact"><svg viewBox="0 0 8 8"><rect x="0.5" y="1.5" width="7" height="5" fill="none" stroke="#1f2a6b" stroke-width=".8"/><path d="M0.5 1.5 L4 4.5 L7.5 1.5" fill="none" stroke="#1f2a6b" stroke-width=".8"/></svg>ib@korven-immobilien.example</p>
          <p class="contact"><svg viewBox="0 0 8 8"><circle cx="4" cy="4" r="3.4" fill="none" stroke="#1f2a6b" stroke-width=".8"/><path d="M0.6 4 H7.4 M4 0.6 V7.4" stroke="#1f2a6b" stroke-width=".6"/></svg>www.korven-immobilien.example</p>
        </div>
      </div>
    </div>
    <h3 class="team-title">Unser <span class="accent">Team</span></h3>
    <div class="team">
      <div class="member"><div class="portrait" role="img" aria-label="Portrait Lorenz A. Korven vor dunklem Hintergrund"></div><p>Lorenz A. Korven</p></div>
      <div class="member"><div class="portrait" role="img" aria-label="Portrait Henrike Weidlich vor dunklem Hintergrund"></div><p>Henrike Weidlich</p></div>
      <div class="member"><div class="portrait" role="img" aria-label="Portrait Jonas Weidlich vor dunklem Hintergrund"></div><p>Jonas Weidlich</p></div>
      <div class="member"><div class="portrait" role="img" aria-label="Portrait Greta Haldenmeier vor dunklem Hintergrund"></div><p>Greta Haldenmeier</p></div>
      <div class="member"><div class="portrait" role="img" aria-label="Portrait Dr. Ilse Brandvoort vor dunklem Hintergrund"></div><p>Dr. Ilse Brandvoort</p></div>
      <div class="member"><div class="portrait" role="img" aria-label="Portrait Mira Sonntag vor dunklem Hintergrund"></div><p>Mira Sonntag</p></div>
    </div>
  </article>
</section>

<section class="set" style="top:1755px">
  <article class="front">
    <div class="photo" role="img" aria-label="Glückliches Paar von hinten vor einer modernen Villa im warmen Abendlicht"></div>
    <svg class="band" width="297" height="418" viewBox="0 0 297 418" style="top:0">
      <polygon points="0,337 297,305 297,418 0,418" fill="#1f2a6b"/>
      <polygon points="0,331 297,299 297,305 0,337" fill="#b48a5a"/>
    </svg>
    <svg class="logo-panel" viewBox="0 0 144 56"><polygon points="0,0 144,0 128,56 0,56" fill="#fff" fill-opacity=".95"/></svg>
    <div class="logo-name">KORVEN</div>
    <p class="claim"><span class="accent">GENIEẞEN</span> SIE IHRE FREIHEIT.<br>WIR VERKAUFEN <span class="accent">IHRE IMMOBILIE.</span></p>
  </article>

  <article class="back">
    <div class="photo" role="img" aria-label="Moderner weißer Bungalow mit Terrasse im Grünen"></div>
    <svg class="band" width="308" height="430" viewBox="0 0 308 430" style="top:0">
      <polygon points="0,90 308,72 308,256 0,251" fill="#1f2a6b"/>
      <polygon points="0,84 308,66 308,72 0,90" fill="#b48a5a"/>
      <polygon points="0,251 308,256 308,342 0,340" fill="#dcdcde"/>
      <polygon points="0,340 308,334 308,430 0,430" fill="#16161a"/>
    </svg>
    <svg class="logo-panel" viewBox="0 0 110 48"><polygon points="0,0 110,0 98,48 0,48" fill="#fff"/></svg>
    <div class="logo-name">KORVEN</div>
    <div class="badge"><span class="w">KOSTENLOSE</span><br><span class="g">IMMOBILIEN<br>BEWERTUNG</span></div>
    <h2 class="title">Das Besondere bei<br><span class="accent">KORVEN Immobilien</span></h2>
    <ul class="usp">
      <li><svg viewBox="0 0 11 12"><path d="M1 5 L4 10 L10 1" fill="none" stroke="#fff" stroke-width="1.6"/></svg>langjährige Erfahrung mit Immobilien des gehobenen Segments</li>
      <li><svg viewBox="0 0 11 12"><path d="M1 5 L4 10 L10 1" fill="none" stroke="#fff" stroke-width="1.6"/></svg>hochprofessionelle Komplettabwicklung in kürzester Zeit</li>
      <li><svg viewBox="0 0 11 12"><path d="M1 5 L4 10 L10 1" fill="none" stroke="#fff" stroke-width="1.6"/></svg>ausgezeichnete Referenzen</li>
      <li><svg viewBox="0 0 11 12"><path d="M1 5 L4 10 L10 1" fill="none" stroke="#fff" stroke-width="1.6"/></svg>auf Wunsch sehr diskrete Abwicklung</li>
    </ul>
    <div class="info">
      <div class="centered" style="top:18px">
        <p class="lead">Für ein freundliches Erstgespräch erreichen Sie uns jederzeit unter:</p>
        <p class="big-phone"><svg viewBox="0 0 8 8"><path d="M1.5 0.8 L3 2.6 L2.2 3.6 Q3.3 5.2 4.4 5.8 L5.4 5 L7.2 6.5 L6.2 7.5 Q2.5 6.8 0.5 1.8 Z" fill="#1f2a6b"/></svg>0157 - 3948 2036</p>
        <div class="row">
          <p class="contact"><svg viewBox="0 0 8 8"><rect x="0.5" y="1.5" width="7" height="5" fill="none" stroke="#1f2a6b" stroke-width=".8"/><path d="M0.5 1.5 L4 4.5 L7.5 1.5" fill="none" stroke="#1f2a6b" stroke-width=".8"/></svg>ib@korven-immobilien.example</p>
          <p class="contact"><svg viewBox="0 0 8 8"><circle cx="4" cy="4" r="3.4" fill="none" stroke="#1f2a6b" stroke-width=".8"/><path d="M0.6 4 H7.4 M4 0.6 V7.4" stroke="#1f2a6b" stroke-width=".6"/></svg>www.korven-immobilien.example</p>
        </div>
      </div>
    </div>
    <h3 class="team-title">Unser <span class="accent">Team</span></h3>
    <div class="team">
      <div class="member"><div class="portrait" role="img" aria-label="Portrait Lorenz A. Korven vor dunklem Hintergrund"></div><p>Lorenz A. Korven</p></div>
      <div class="member"><div class="portrait" role="img" aria-label="Portrait Henrike Weidlich vor dunklem Hintergrund"></div><p>Henrike Weidlich</p></div>
      <div class="member"><div class="portrait" role="img" aria-label="Portrait Jonas Weidlich vor dunklem Hintergrund"></div><p>Jonas Weidlich</p></div>
      <div class="member"><div class="portrait" role="img" aria-label="Portrait Greta Haldenmeier vor dunklem Hintergrund"></div><p>Greta Haldenmeier</p></div>
      <div class="member"><div class="portrait" role="img" aria-label="Portrait Dr. Ilse Brandvoort vor dunklem Hintergrund"></div><p>Dr. Ilse Brandvoort</p></div>
      <div class="member"><div class="portrait" role="img" aria-label="Portrait Mira Sonntag vor dunklem Hintergrund"></div><p>Mira Sonntag</p></div>
    </div>
  </article>
</section>

</body>
</html>
```